もみほぐし、マッサージ店の看板デザイン(二種類)を依頼させて頂きます。

1.店舗に設置するヨコ看板   横350cm×縦75cm
2.店外に設置するスタンド看板 横42cm×縦113cm
(設置位置は添付画像をご覧ください、また参考程度に添付エクセルをご覧くださいませ)

場所は、県では一番賑わっているアーケード内の繁華街となります。
誰でもお越しいただける「安心感、癒し、やわらかさ」と
街中ですので「多少の洗練」を希望いたします。
一目で「マッサージ、指圧、もみほぐし」と直感できると嬉しいです。

店内は明るいライムグリーンを基調としておりますが、
ブランド力はありませんので、目につきやすい配色で人目を引ければと思います。

準備中ではございますが、店内の画像も添付いたしましたのでご覧ください。

会社名  フワリK 桜木通り店
電話番号 096-555-0172
営業時間 朝10時から翌朝5時

・「全身ほぐしコース 60分 税込 2980円」

・価格テーブル(添付エクセルデータをご覧ください)

・「深夜0時以降は、プラス100円いただきます」

・エレベータをのぼって2階にあるため「2F」

・ロゴ等はなにぶん開業前ですので、特にございません。

文言で強調していただきたいポイントは
「全身ほぐしコース60分2980円」の割安感と
2回にあるため「2F」というところです。
明るめのライムグリーン、強調する意味での赤など。他にも良い案をご提案下さい。
なにぶん初めての依頼ですので、いたらない部分もあるかと思いますが、誠実に対応させていただきますので、どうぞよろしくお願いいたします。
すみません。
記載項目の記述は、スタンド看板だけを念頭に置いて書いてしまいました。

ヨコ看板に最低限載せていただきたい記載文言は

・店舗名 フワリK 桜木通店
・全身(※もみ)ほぐし(※コース)60分 税込 2980円
・電話番号 096-555-0172

の3つとなります(※は必須ではございません)
よろしくお願いいたします。
時間も差し迫ったところで、申し訳ございませんが、
強く希望させていただきたいポイントと
変更内容を追記いたします。

【希望】
1)上部のヨコ看板についてですが
店名等より「全身もみほぐし 60分 2980円(税込)」
という文言を、より大きく前面に押し出していただきたいです。
(税込)もお願いいたします。

2)下のスタンド看板についてです。
価格テーブルを必ず載せて欲しいです。
(もみほぐし)(足つぼ)(もみほぐし&足つぼハーフ)(眼精疲労コース)
以上の4種類です。

3)写真についての希望です。
当店ではお客様任意の動きやすい服装か、ジャージをお貸しして
その上からタオルを載せて施術するという形をとりますので
素材がございましたら、着衣の画像をお願いいたします。
これはあくまで希望で必須ではありません。

4)店名について。
「フワリ」はカタカナ。「M」はアルファベットをお願いいたします。

【変更】
眼精疲労コースの時間と料金を変更いたします。
「15分1080円」となります。
価格テーブルのエクセルファイルをアップロードいたしますのでご覧ください。

以上よろしくお願い申し上げます。
こちらの説明不足でご迷惑をおかけします。
(マッサージ)という言葉が法律に抵触する可能性も考えられます。
(マッサージ)という単語は看板では使わない方向で考えておりますので
よろしくお願いいたします。
募集終了後、当選候補者様をお選びし修正依頼を
お送り致しますが少々急いでおりますので納品を
明日、11日15時までにお願いしたいと考えております。
もし修正依頼を受け取られた候補者様のスケジュールが
合わず、11日15時に間に合わないと判断された場合は
即座にお断りのご連絡を頂けましたら幸いです。
こちらの勝手な都合を押しつけるようで誠に恐縮ですが
よろしく申し上げます。

配色、デザインが最も洗練されていると感じました。
一目で気に入りました。
親指を鳥の目に見立てた「M」のロゴマークも素晴らしいと思いました。

こちらの度重なる修正依頼にも迅速に、誠実に対応して頂きました。

予想を超えるご応募をいただき誠に感謝しております。
たくさん良いデザインがありましたので一つお選びするのは
大変心苦しかったです。

皆さまありがとうございました。

```html
<!DOCTYPE html>
<html lang="ja">
<head>
<meta charset="utf-8">
<title>フワリK 桜木通り店 スタンド看板</title>
<link rel="stylesheet" href="https://fonts.googleapis.com/css2?family=M+PLUS+1p:wght@500;700;800;900&family=Noto+Serif+JP:wght@700;900&display=swap">
<style>
:root{
  --green-deep:#3f8a1e;
  --green:#6fb52c;
  --green-light:#b8dc6e;
  --green-pale:#e9f5cf;
  --red:#e0141b;
  --orange:#ef6a10;
  --brown:#6b4a2a;
  --white:#ffffff;
  --gray:#555555;
  --grid:#c9dcae;
}
*{margin:0;padding:0;box-sizing:border-box}
html,body{width:1200px;height:3224px;overflow:hidden}
body{font-family:"M PLUS 1p",sans-serif;background:var(--white)}
.sign{position:relative;width:1200px;height:3224px;overflow:hidden;
  background:linear-gradient(180deg,#f4fae6 0px,#cfe89a 380px,var(--green) 900px,var(--green) 2200px,#8cc63f 2700px,#dff0bb 3000px,#f3f9e6 3224px)}
.photo{position:absolute;left:220px;top:-340px;width:760px;height:760px;border-radius:50%;
  background:radial-gradient(circle at 50% 60%,#f6e2d3 0%,#e9c6ad 45%,#f3f3f1 75%);
  box-shadow:0 0 60px 30px rgba(255,255,255,.85)}
.headline{position:absolute;top:490px;left:0;width:1200px;text-align:center;
  font-weight:900;font-size:124px;letter-spacing:4px;color:var(--white);
  -webkit-text-stroke:10px var(--green-deep);paint-order:stroke fill;
  text-shadow:0 6px 10px rgba(0,60,0,.35)}
.offer{position:absolute;top:760px;left:60px;width:1080px;height:200px}
.offer-time{position:absolute;left:10px;top:60px;width:180px;height:96px;border-radius:48px;
  background:var(--green-deep);color:var(--white);font-weight:800;font-size:64px;
  line-height:96px;text-align:center}
.offer-price{position:absolute;left:230px;top:0;font-weight:900;font-size:200px;line-height:200px;
  color:var(--red);-webkit-text-stroke:10px var(--white);paint-order:stroke fill;letter-spacing:2px}
.offer-price small{font-size:80px}
.price-table{position:absolute;left:60px;top:1032px;width:1080px;height:1080px;
  display:grid;grid-template-columns:200px 293px 293px 294px;grid-template-rows:160px repeat(6,153px);
  background:rgba(255,255,255,.92);border:3px solid var(--grid)}
.cell{border-right:3px solid var(--grid);border-bottom:3px solid var(--grid);
  display:flex;align-items:center;justify-content:center;text-align:center}
.cell.head{font-size:38px;font-weight:700;color:var(--green-deep);line-height:1.2;background:rgba(233,245,207,.7)}
.cell.time{font-size:46px;font-weight:700;color:var(--gray)}
.cell.price{font-size:66px;font-weight:900;color:var(--red)}
.cell.price small{font-size:28px;margin-left:4px;margin-top:22px}
.cell.none{background:linear-gradient(to top right,transparent calc(50% - 2px),var(--grid) calc(50% - 2px),var(--grid) calc(50% + 2px),transparent calc(50% + 2px))}
.extra{position:absolute;left:60px;width:1080px;color:var(--white);font-weight:700}
.extra.eye{top:2130px;font-size:46px;display:flex;align-items:center}
.extra.eye .dots{flex:1;border-bottom:4px dotted rgba(255,255,255,.8);margin:0 24px}
.extra.eye b{font-weight:900}
.extra.night{top:2200px;font-size:38px;color:#fff7c0}
.shop{position:absolute;left:60px;top:2340px;width:1080px;height:520px;border-radius:30px;
  background:linear-gradient(180deg,#ffffff 0%,var(--green-pale) 100%);box-shadow:0 6px 16px rgba(0,60,0,.25)}
.floor{position:absolute;left:380px;top:2288px;width:440px;height:132px;border-radius:66px;
  background:var(--orange);border:8px solid var(--white);color:var(--white);
  font-weight:900;font-size:110px;line-height:116px;text-align:center}
.shop-name{position:absolute;left:0;top:160px;width:1080px;text-align:center;
  font-family:"Noto Serif JP",serif;font-weight:900;font-size:190px;color:var(--green-deep);letter-spacing:10px}
.branch{position:absolute;left:150px;top:400px;width:780px;height:80px;background:var(--brown);
  color:var(--white);font-family:"Noto Serif JP",serif;font-weight:700;font-size:54px;line-height:80px;
  text-align:center;letter-spacing:8px}
.hours{position:absolute;left:0;top:2930px;width:1200px;text-align:center;font-weight:800;font-size:60px;
  color:var(--white);-webkit-text-stroke:6px var(--green-deep);paint-order:stroke fill}
.hours b{font-size:84px;font-weight:900}
.phone{position:absolute;left:0;top:3070px;width:1200px;display:flex;justify-content:center;align-items:center;
  gap:20px;color:var(--red);font-weight:900;font-size:122px;line-height:140px}
.phone svg{width:100px;height:100px}
</style>
</head>
<body>
<div class="sign">
  <div class="photo" role="img" aria-label="足裏をもみほぐす施術の写真"></div>

  <h1 class="headline">全身もみほぐし</h1>

  <div class="offer">
    <div class="offer-time">60分</div>
    <div class="offer-price">2,980<small>円</small></div>
  </div>

  <div class="price-table">
    <div class="cell head"></div>
    <div class="cell head">もみほぐし</div>
    <div class="cell head">足ツボ</div>
    <div class="cell head">もみほぐし<br>&amp;足ツボ</div>

    <div class="cell time">15 分</div>
    <div class="cell price">980<small>円</small></div>
    <div class="cell none"></div>
    <div class="cell none"></div>

    <div class="cell time">30 分</div>
    <div class="cell price">1,780<small>円</small></div>
    <div class="cell price">2,280<small>円</small></div>
    <div class="cell none"></div>

    <div class="cell time">45 分</div>
    <div class="cell price">2,480<small>円</small></div>
    <div class="cell price">2,980<small>円</small></div>
    <div class="cell none"></div>

    <div class="cell time">60 分</div>
    <div class="cell price">2,980<small>円</small></div>
    <div class="cell price">3,580<small>円</small></div>
    <div class="cell price">3,380<small>円</small></div>

    <div class="cell time">90 分</div>
    <div class="cell price">4,680<small>円</small></div>
    <div class="cell price">5,380<small>円</small></div>
    <div class="cell price">4,980<small>円</small></div>

    <div class="cell time">120 分</div>
    <div class="cell price">6,280<small>円</small></div>
    <div class="cell price">7,180<small>円</small></div>
    <div class="cell price">6,680<small>円</small></div>
  </div>

  <p class="extra eye">■眼精疲労コース<span class="dots"></span>15分 <b>&nbsp;1,780円</b></p>
  <p class="extra night">☆深夜 12 時以降は、合計金額よりプラス１００円頂きます。</p>

  <div class="shop">
    <div class="shop-name">フワリK</div>
    <div class="branch">桜木通り店</div>
  </div>
  <div class="floor">2F</div>

  <p class="hours">営業時間：朝 <b>10</b> 時から翌朝 <b>5</b> 時</p>

  <p class="phone">
    <svg viewBox="0 0 24 24" aria-hidden="true"><path fill="currentColor" d="M6.6 10.8a15.1 15.1 0 0 0 6.6 6.6l2.2-2.2a1 1 0 0 1 1-.25 11.4 11.4 0 0 0 3.6.57 1 1 0 0 1 1 1V20a1 1 0 0 1-1 1A17 17 0 0 1 3 4a1 1 0 0 1 1-1h3.5a1 1 0 0 1 1 1c0 1.25.2 2.45.57 3.57a1 1 0 0 1-.25 1z"/></svg>
    096-555-0172
  </p>
</div>
</body>
</html>
```